Family cosmetic dental practice. Very friendly, relaxed environment. All aspects of modern dentistry with exceptional service.

Industry/Entity Type

Dental

Contact Information for Business Card

Owen T Harrow DMD, P.C. 814-507-6192
418 WEST KELLAND
LARKIN FALLS, KL side2- www.harrowdental.net/drowenharrow for news, free KRV Football tickets, promotions, etc.

Requirements
Must have
• face of male and female showing attractive smiles.

```html
<!DOCTYPE html>
<html lang="en">
<head>
<meta charset="utf-8">
<title>Owen T Harrow DMD, P.C. – Business Card</title>
<link rel="stylesheet" href="https://fonts.googleapis.com/css2?family=Questrial&display=swap">
<style>
  :root {
    --backdrop: #b4b4b4;
    --sky-blue: #4ac0ef;
    --deep-blue: #0ea7e1;
    --name-blue: #1ba3dc;
    --white: #ffffff;
    --sand: #eef3f2;
  }
  * { margin: 0; padding: 0; box-sizing: border-box; }
  html, body { width: 1200px; height: 1000px; overflow: hidden; }
  body {
    background: var(--backdrop);
    font-family: "Questrial", "Century Gothic", sans-serif;
    position: relative;
  }
  .card {
    position: absolute;
    width: 720px;
    height: 420px;
    overflow: hidden;
    box-shadow: 0 6px 18px rgba(0,0,0,0.25);
  }
  /* Front side */
  .card-front { left: 150px; top: 50px; }
  .beach-photo {
    position: absolute; inset: 0;
    background:
      linear-gradient(90deg, rgba(255,255,255,0) 0%, rgba(255,255,255,0) 48%, rgba(240,228,222,0.55) 62%, rgba(225,205,190,0.6) 100%),
      linear-gradient(180deg, #7cc4ea 0%, #b9def2 22%, #66c9dc 30%, #8ad7df 48%, var(--sand) 72%, #e7ece9 100%);
  }
  .practice-name {
    position: absolute; left: 45px; top: 140px;
    color: var(--name-blue);
  }
  .practice-name .doctor {
    font-size: 44px; line-height: 1; letter-spacing: 0.5px;
    padding-bottom: 4px;
    border-bottom: 2px solid var(--name-blue);
    width: 330px;
    white-space: nowrap;
  }
  .practice-name .credentials {
    font-size: 24px; margin-top: 4px; padding-left: 2px; letter-spacing: 1px;
  }
  .contact-panel {
    position: absolute; left: 28px; top: 240px;
    width: 345px; height: 180px;
    background: var(--sky-blue);
    color: var(--white);
    padding: 24px 0 0 36px;
  }
  .contact-panel .phone {
    display: flex; align-items: center; gap: 8px;
    font-size: 24px;
  }
  .contact-panel .phone svg { width: 26px; height: 26px; flex: none; }
  .contact-panel .address {
    margin-top: 10px; padding-left: 32px;
    font-size: 15px; line-height: 1.3;
  }
  /* Back side */
  .card-back { left: 320px; top: 520px; background: var(--white); }
  .back-band {
    position: absolute; left: 0; top: 0; width: 100%; height: 310px;
    background: var(--sky-blue);
  }
  .web-link {
    position: absolute; left: 62px; top: 50px;
    color: var(--white); font-size: 22px; letter-spacing: 0.5px;
    white-space: nowrap;
  }
  .offer-box {
    position: absolute; left: 14px; top: 86px;
    width: 376px; height: 165px;
    background: var(--deep-blue);
    color: var(--white);
    padding: 20px 0 0 42px;
    font-size: 33px; line-height: 1.08;
  }
</style>
</head>
<body>
  <section class="card card-front">
    <div class="beach-photo" role="img" aria-label="Photo of a smiling young couple on a sunny tropical beach with turquoise sea and blue sky"></div>
    <div class="practice-name">
      <div class="doctor">Owen T Harrow</div>
      <div class="credentials">DMD, P.C.</div>
    </div>
    <div class="contact-panel">
      <div class="phone">
        <svg viewBox="0 0 26 26" aria-hidden="true">
          <circle cx="13" cy="13" r="11.5" fill="none" stroke="#fff" stroke-width="2"/>
          <path d="M9 7.5c.8-.5 1.6-.4 2 .3l1.1 2c.3.6.1 1.2-.4 1.6l-.7.5c.6 1.5 1.6 2.6 3 3.3l.6-.6c.4-.5 1.1-.6 1.6-.3l1.9 1.2c.6.4.7 1.2.2 1.9-.8 1.1-2 1.5-3.2 1-3.3-1.3-5.6-3.8-6.7-7.1-.4-1.3.1-2.3.6-2.8z" fill="#fff"/>
        </svg>
        <span>814-507-6192</span>
      </div>
      <p class="address">418 West Kelland Ridge,<br>Larkin Falls, KL</p>
    </div>
  </section>

  <section class="card card-back">
    <div class="back-band"></div>
    <p class="web-link">www.harrowdental.net/drowenharrow</p>
    <div class="offer-box">
      <p>Free KRV</p>
      <p>Football tickets</p>
      <p>promotions, etc.</p>
    </div>
  </section>
</body>
</html>
```